mh ridgeline excursions website for fish guide business in Campbell river Bc

looking for website to promote my fishing guide buisiness and its charters

Have uploaded a pictures of my boat not sure which one…
Also two pictures of a fish caught and one of a fish cleaning station

Have added script for website

Target Market(s)

Visitors to Campbell River BC who want fish and or go whale / wildlife adventure tour

Industry/Entity Type

Tourism

Coding

Coded - Design and coding required

Number of Pages Required

5+ page

Font styles to use
Sans Serif

Requirements
Must have
• New email is info@mhridgelineexcursions…. Delete the word halibut…. Add second contact Wes 250-731-6924….Pictures and my logo … place for videos
Should not have
• should not have a boat picture which is not supplied

```html
<!DOCTYPE html>
<html lang="en">
<head>
<meta charset="utf-8">
<title>MH Ridgeline Excursions – Campbell River Fishing &amp; Wildlife Charters</title>
<link rel="stylesheet" href="https://fonts.googleapis.com/css2?family=Poppins:wght@400;500;600;700&family=Rubik:wght@500;600&display=swap">
<style>
:root{
  --navy:#2b2668;
  --navy-deep:#252060;
  --ink:#1d1d1f;
  --body:#4a4a55;
  --mist:#f3f2fa;
  --white:#ffffff;
  --footer:#2b2b2b;
  --footer-line:#4a4a4a;
}
*{margin:0;padding:0;box-sizing:border-box}
html,body{width:1200px;height:5310px;overflow:hidden}
body{font-family:"Poppins",sans-serif;color:var(--body);background:var(--white);position:relative}
.section{position:absolute;left:0;width:1200px}
h1,h2{font-family:"Rubik",sans-serif;font-weight:500;color:var(--ink);letter-spacing:.2px}
h2{font-size:40px;line-height:50px}
.accent{position:relative;display:inline-block}
.accent::after{content:"";position:absolute;left:0;bottom:-10px;width:48px;height:3px;background:var(--navy);border-radius:2px}
.center .accent::after{left:50%;transform:translateX(-50%)}
p{font-size:16.5px;line-height:29px}
.link{color:var(--navy);font-weight:600;text-decoration:underline}

/* hero */
.hero{top:0;height:703px;background:linear-gradient(100deg,#d9772a 0%,#c98c3c 20%,#8a8a45 45%,#55703a 65%,#6d8a5a 80%,#a7b9c2 100%)}
.hero::after{content:"";position:absolute;left:0;right:0;bottom:0;height:240px;background:linear-gradient(180deg,rgba(60,70,40,0) 0%,rgba(70,60,30,.35) 100%)}
.brand{position:absolute;left:111px;top:46px;display:flex;align-items:center;gap:10px;z-index:2}
.brand-mark{width:58px;height:58px;border-radius:50%;background:var(--white);border:4px solid var(--navy);flex:none}
.brand-name{font-family:"Poppins",sans-serif;font-weight:700;font-size:13px;color:var(--navy);line-height:17px;width:110px}
.nav{position:absolute;left:305px;top:66px;display:flex;gap:26px;z-index:2}
.nav a{font-size:13.5px;font-weight:600;color:#33334a;text-decoration:none;text-transform:uppercase;letter-spacing:.3px}
.nav a.active{color:var(--navy)}
.btn{display:inline-block;background:var(--navy);color:var(--white);font-weight:600;text-transform:uppercase;border-radius:30px;text-decoration:none;text-align:center}
.btn-top{position:absolute;left:773px;top:54px;width:151px;height:46px;line-height:46px;font-size:13px;z-index:2}
.socials{position:absolute;display:flex;gap:12px;z-index:2}
.socials span{display:block;width:34px;height:34px;border-radius:50%;border:2px solid var(--white)}
.hero .socials{left:963px;top:60px}
.hero-photo{position:absolute;left:560px;top:0;width:640px;height:703px;background:linear-gradient(180deg,rgba(150,160,120,.4),rgba(120,110,80,.2))}
.hero-title{position:absolute;left:111px;top:300px;font-family:"Rubik",sans-serif;font-weight:600;font-size:41px;line-height:51px;color:var(--white);z-index:2}
.btn-hero{position:absolute;left:111px;top:480px;width:270px;height:46px;line-height:46px;font-size:13px;z-index:2}
.dots{position:absolute;left:548px;top:656px;display:flex;gap:12px;z-index:2}
.dots span{width:18px;height:18px;border-radius:50%;border:2px solid var(--white)}
.dots span.on{background:radial-gradient(circle,var(--white) 0 3px,transparent 4px)}

/* intro */
.intro{top:703px;height:445px;background:var(--mist);text-align:center}
.intro h2{position:absolute;left:0;right:0;top:95px}
.intro p{position:absolute;left:160px;right:160px;top:240px;font-size:17px;line-height:30px}

/* feature rows */
.photo-ring{position:absolute;width:428px;height:428px;border-radius:50%;border:6px solid var(--navy);padding:10px;background:var(--white)}
.photo-ring .fill{width:100%;height:100%;border-radius:50%}
.feature-text{position:absolute;width:486px}
.feature-text h2{margin-bottom:44px}
.feature-text p{text-align:justify}

/* wildlife */
.wildlife{top:2237px;height:516px;background:linear-gradient(180deg,#fbfbfc 0%,#f1f2f3 40%,#c5c9cc 62%,#7d878c 80%,#4c5a5e 100%);text-align:center}
.wildlife h2{position:absolute;left:0;right:0;top:107px}
.wildlife p{position:absolute;left:160px;right:160px;top:196px;font-size:16.5px}

/* cta */
.cta{top:3390px;height:402px;background:var(--navy-deep);text-align:center}
.cta h2{color:var(--white);position:absolute;left:0;right:0;top:111px}
.cta h2 .accent::after{background:var(--white)}
.cta p{color:var(--white);position:absolute;left:140px;right:140px;top:199px;font-size:17px;line-height:30px}
.cta .link{color:var(--white)}

/* footer */
.footer{top:4939px;height:371px;background:var(--footer);color:var(--white);text-align:center}
.footer-brand{position:absolute;left:0;right:0;top:44px;display:flex;flex-direction:column;align-items:center;gap:10px}
.footer-brand .brand-mark{width:60px;height:60px;border-color:var(--white);background:transparent}
.footer-brand .brand-name{color:var(--white);width:auto;font-size:14px}
.footer-nav{position:absolute;left:0;right:0;top:184px;display:flex;justify-content:center;font-size:14.5px;font-weight:600}
.footer-nav a{color:var(--white);text-decoration:none;padding:0 34px;border-left:2px solid var(--white);line-height:16px}
.footer-nav a:first-child{border-left:none}
.footer-contact{position:absolute;left:0;right:0;top:222px;display:flex;justify-content:center;align-items:center;gap:12px;font-size:13.5px}
.footer-contact svg{vertical-align:middle;margin-right:6px}
.footer .socials{left:534px;top:262px}
.footer .socials span{width:36px;height:36px}
.footer-rule{position:absolute;left:111px;right:111px;top:318px;height:1px;background:var(--footer-line)}
.copyright{position:absolute;left:0;right:0;top:336px;font-size:12.5px}
</style>
</head>
<body>

<header class="section hero">
  <div class="hero-photo" role="img" aria-label="Angler standing on the bow of a boat casting a rod over a calm sunlit lake"></div>
  <div class="brand"><span class="brand-mark"></span><span class="brand-name">MH Ridgeline Excursions</span></div>
  <nav class="nav">
    <a class="active" href="#">Home</a><a href="#">About Us</a><a href="#">Services</a><a href="#">Blog</a><a href="#">Contact Us</a>
  </nav>
  <a class="btn btn-top" href="#">Get Started</a>
  <div class="socials"><span></span><span></span><span></span></div>
  <h1 class="hero-title">Discover Your<br>Thrilling West Coast<br>Adventure</h1>
  <a class="btn btn-hero" href="#">Book Your Charter Today!</a>
  <div class="dots"><span></span><span class="on"></span><span></span><span></span></div>
</header>

<section class="section intro center">
  <h2>Experience the Ultimate West<br><span class="accent">Coast Adventure</span></h2>
  <p>Welcome aboard the 22-foot Harbourline charter boat, where MH Ridgeline Excursions and the legendary Cole Brennan await to take you on an unforgettable journey through the untamed beauty of Campbell River, British Columbia. Brace yourself for an adrenaline-pumping fishing and wildlife tour like no other!</p>
</section>

<section class="section" style="top:1148px;height:1089px">
  <div class="photo-ring" style="left:111px;top:110px"><div class="fill" role="img" aria-label="Charter boat moored at a marina dock" style="background:linear-gradient(160deg,#7fa3c4 0%,#cfd9e0 45%,#f2f4f5 60%,#2f5d7a 100%)"></div></div>
  <div class="feature-text" style="left:604px;top:182px">
    <h2>Reel in Your<br><span class="accent">Dream Catch</span></h2>
    <p>With Cole Brennan's expert guidance, you'll have the chance to reel in monstrous salmon and feisty cod. Prepare for an angler's dream come true as you witness the sheer power and excitement of landing your prized catch.</p>
  </div>

  <div class="feature-text" style="left:111px;top:672px">
    <h2>Wild Encounters<br><span class="accent">with Ocean Giants</span></h2>
    <p>Immerse yourself in the awe-inspiring world of marine life. Get up close and personal with majestic humpback whales as they breach just a splash away from the boat. Glide alongside graceful orcas as they glide effortlessly through the waves. This is a once-in-a-lifetime opportunity to witness the magic of these gentle ocean giants in their natural habitat.</p>
  </div>
  <div class="photo-ring" style="left:660px;top:629px"><div class="fill" role="img" aria-label="Angler holding a large salmon on the boat deck" style="background:linear-gradient(170deg,#a9c1d8 0%,#5f7f98 40%,#40505a 70%,#c9cdd0 100%)"></div></div>
</section>

<section class="section wildlife center" role="img" aria-label="Kayaker paddling on a misty lake between forested hills">
  <h2><span class="accent">Awe-Inspiring Wildlife Moments</span></h2>
  <p>Venture into the heart of the wilderness, where coastal bears fish for salmon, showcasing their incredible hunting skills. Look up to the sky as bald eagles soar with breathtaking elegance overhead. These captivating wildlife moments are sure to leave you speechless.</p>
</section>

<section class="section" style="top:2753px;height:637px">
  <div class="photo-ring" style="left:111px;top:101px"><div class="fill" role="img" aria-label="Guide seated in the stern of the boat with prawn traps" style="background:linear-gradient(170deg,#6f9fd0 0%,#a8c4dc 35%,#6b7f6a 55%,#dcdfe2 100%)"></div></div>
  <div class="feature-text" style="left:604px;top:210px">
    <h2>Prawning Adventure<br><span class="accent">and Delicious Rewards</span></h2>
    <p>Experience the thrill of pulling up prawn traps, brimming with delectable, fresh prawns ready to be savored. Take home a delicious bounty and share the taste of the West Coast with your loved ones over a special dinner.</p>
  </div>
</section>

<section class="section cta center">
  <h2>Act Now - <span class="accent">Limited</span> Slots Available!</h2>
  <p>Don't miss out on this epic adventure - time is running out! The demand for our charters is soaring, and spots are filling up fast. Contact Cole Brennan at <span class="link">250-286-5130</span> or Wes at <span class="link">250-731-6924</span>, or email <span class="link">info@mhridgelineexcursions.com</span> to secure your spot and create legendary memories.</p>
</section>

<section class="section" style="top:3792px;height:1147px">
  <div class="feature-text" style="left:111px;top:221px">
    <h2>Answer the Call<br><span class="accent">of the Wild</span></h2>
    <p style="text-align:left">The untamed wilderness of Campbell River beckons you. Answer the call of the wild and embark on a journey that will ignite your sense of adventure and wonder.</p>
  </div>
  <div class="photo-ring" style="left:660px;top:101px"><div class="fill" role="img" aria-label="Two anglers working rods on the boat deck" style="background:linear-gradient(170deg,#4f8bd0 0%,#9ec0e0 35%,#3e6da8 55%,#6e8a5c 100%)"></div></div>

  <div class="photo-ring" style="left:111px;top:600px"><div class="fill" role="img" aria-label="Outboard motor at the stern of the boat with a wake behind it" style="background:linear-gradient(170deg,#8fb4dc 0%,#3f5b52 35%,#587a96 55%,#e3e6e8 100%)"></div></div>
  <div class="feature-text" style="left:604px;top:682px">
    <h2>Book Your Thrilling<br><span class="accent">Charter Today!</span></h2>
    <p>Your heart-pounding West Coast adventure is just a call away! Grab your phone and dial <span class="link">250-286-5130</span> or Wes at <span class="link">250-731-6924</span>, or email <span class="link">info@mhridgelineexcursions.com</span> to lock in your spot. Cole Brennan and MH Ridgeline Excursions are ready to make your dreams of an exhilarating West Coast experience come true.</p>
  </div>
</section>

<footer class="section footer">
  <div class="footer-brand"><span class="brand-mark"></span><span class="brand-name">MH Ridgeline Excursions</span></div>
  <nav class="footer-nav"><a href="#">HOME</a><a href="#">ABOUT US</a><a href="#">SERVICES</a><a href="#">BLOG</a><a href="#">CONTACT US</a></nav>
  <div class="footer-contact">
    <span><svg width="13" height="13" viewBox="0 0 24 24" fill="#9a9a9a"><path d="M6.6 10.8c1.4 2.8 3.8 5.1 6.6 6.6l2.2-2.2c.3-.3.7-.4 1-.2 1.1.4 2.3.6 3.6.6.6 0 1 .4 1 1V20c0 .6-.4 1-1 1C10.6 21 3 13.4 3 4c0-.6.4-1 1-1h3.5c.6 0 1 .4 1 1 0 1.3.2 2.5.6 3.6.1.3 0 .7-.2 1z"/></svg>250-286-5130</span>
    <span>|</span>
    <span><svg width="13" height="13" viewBox="0 0 24 24" fill="#9a9a9a"><path d="M6.6 10.8c1.4 2.8 3.8 5.1 6.6 6.6l2.2-2.2c.3-.3.7-.4 1-.2 1.1.4 2.3.6 3.6.6.6 0 1 .4 1 1V20c0 .6-.4 1-1 1C10.6 21 3 13.4 3 4c0-.6.4-1 1-1h3.5c.6 0 1 .4 1 1 0 1.3.2 2.5.6 3.6.1.3 0 .7-.2 1z"/></svg>Wes 250-731-6924</span>
    <span>|</span>
    <span><svg width="14" height="11" viewBox="0 0 24 18" fill="#9a9a9a"><path d="M0 0h24v18H0z" opacity=".9"/><path d="M0 0l12 9 12-9" fill="none" stroke="#2b2b2b" stroke-width="2"/></svg>info@mhridgelineexcursions.com</span>
  </div>
  <div class="socials"><span></span><span></span><span></span></div>
  <div class="footer-rule"></div>
  <div class="copyright">© 2023 <strong>MH RIDGELINE EXCURSIONS</strong> &nbsp;|&nbsp; All Rights Reserved</div>
</footer>

</body>
</html>
```